RHPW (Thorough Stomach Clinic of Bramford)

We need a business card design for a new medical group that specializes in Gastroenterology (digestive diseases). We need a double sided card that is professional yet modern.
The front would incorporate our logo, names, titles and contact info. In the back we would like a map to our office as well as a space to write a follow up appointment.
Our address is:
4172 E. Harlow Ave, Suite 615, Las Vegas, NV 89120
phone: (702) 555-0147
fax: (702) 555-0192
website: www.quillmorehealth.example
Target Market(s)
Physicians and patients
Industry/Entity Type
Medical
Contact Information for Business Card
Name
Title
phone: (702) 555-0147
fax: (702) 555-0192
Look and feel

```html
<!DOCTYPE html>
<html lang="en">
<head>
<meta charset="utf-8">
<title>RHPW Business Card</title>
<link href="https://fonts.googleapis.com/css2?family=Arimo:wght@400;700&family=Open+Sans:wght@400;700&display=swap" rel="stylesheet">
<style>
  :root{
    --bg:#ece8e2;
    --card:#fbfbfb;
    --band:#1c5fa6;
    --band-light:#5f97cc;
    --ink:#1b1b1b;
    --muted:#4a4a4a;
    --accent:#2a7fd4;
    --logo:#3a4fa8;
    --map-a:#e9ecef;
    --map-b:#d7dce2;
  }
  *{box-sizing:border-box;margin:0;padding:0}
  html,body{width:1200px;height:902px;overflow:hidden;background:var(--bg)}
  .canvas{position:relative;width:1200px;height:902px}
  .card{
    position:absolute;width:620px;height:354px;background:var(--card);
    box-shadow:0 6px 18px rgba(0,0,0,.18),0 0 0 1px rgba(0,0,0,.04);
    overflow:hidden;
  }
  .card--back{left:60px;top:60px}
  .card--front{left:520px;top:488px}
  .band-left{
    position:absolute;left:0;top:0;bottom:0;width:112px;
    background:linear-gradient(90deg,var(--band) 0%,var(--band) 45%,var(--band-light) 100%);
  }
  .band-right{position:absolute;right:0;top:0;bottom:0;width:48px;background:var(--band)}
  .logo{
    position:absolute;font-family:"Arimo",sans-serif;font-weight:700;
    color:var(--logo);letter-spacing:2px;white-space:nowrap;
  }
  .card--back .logo{left:190px;top:26px;font-size:42px}
  .map{
    position:absolute;left:150px;top:96px;width:400px;height:228px;
    background:linear-gradient(135deg,var(--map-a),var(--map-b));
    border-radius:2px;
  }
  .card--front .logo{left:190px;top:74px;font-size:48px}
  .person{
    position:absolute;left:120px;top:196px;width:182px;text-align:right;
    font-family:"Open Sans",sans-serif;color:var(--muted);white-space:nowrap;
  }
  .person__name{font-weight:700;font-size:20px;color:#333}
  .person__title{font-size:17px}
  .divider{position:absolute;left:314px;top:168px;width:2px;height:96px;background:var(--accent)}
  .contacts{
    position:absolute;left:328px;top:166px;list-style:none;
    font-family:"Arimo",sans-serif;font-size:15px;color:var(--ink);white-space:nowrap;
  }
  .contacts li{display:flex;align-items:center;gap:8px;height:26px}
  .contacts svg{width:14px;height:14px;flex:none}
  .address{
    position:absolute;left:140px;top:298px;white-space:nowrap;
    font-family:"Arimo",sans-serif;font-size:17px;color:var(--ink);
  }
</style>
</head>
<body>
<div class="canvas">

  <section class="card card--back">
    <div class="band-left"></div>
    <div class="band-right"></div>
    <div class="logo">RHPW</div>
    <div class="map" role="img" aria-label="Street map showing the office location at 4172 E. Harlow Ave with surrounding roads and freeway"></div>
  </section>

  <section class="card card--front">
    <div class="band-left"></div>
    <div class="band-right"></div>
    <div class="logo">RHPW</div>
    <div class="person">
      <div class="person__name">Dale Whitcomb</div>
      <div class="person__title">Director</div>
    </div>
    <div class="divider"></div>
    <ul class="contacts">
      <li>
        <svg viewBox="0 0 14 14"><rect width="14" height="14" rx="2" fill="#111"/><path d="M4 3.5c.6-.5 1.3 0 1.6.7l.5 1c.2.4 0 .8-.3 1l-.5.4c.4 1 1.1 1.7 2.1 2.1l.4-.5c.3-.3.7-.4 1-.2l1 .5c.7.3 1.1 1 .6 1.6-.8.9-2.2 1-3.6.1A9 9 0 0 1 3.8 7c-.9-1.4-.7-2.7.2-3.5z" fill="#fff"/></svg>
        (702) 555-0147
      </li>
      <li>
        <svg viewBox="0 0 14 14"><rect width="14" height="14" rx="2" fill="#111"/><rect x="3" y="5" width="8" height="6" fill="#fff"/><rect x="4.5" y="2.5" width="5" height="3" fill="#fff"/><rect x="4.5" y="7" width="5" height="1" fill="#111"/></svg>
        (702) 555-0192
      </li>
      <li>
        <svg viewBox="0 0 14 14"><rect width="14" height="14" rx="2" fill="#111"/><circle cx="7" cy="7" r="4" fill="none" stroke="#fff" stroke-width="1.2"/><path d="M3 7h8M7 3c-1.5 2-1.5 6 0 8M7 3c1.5 2 1.5 6 0 8" stroke="#fff" stroke-width=".8" fill="none"/></svg>
        www.quillmorehealth.example
      </li>
    </ul>
    <div class="address">4172 E. Harlow Ave, Suite 615, Las Vegas, NV 89120</div>
  </section>

</div>
</body>
</html>
```